Lost Teens Auto Doantion Website Design

Please create a new one page website design.

Current site: http://autosforyouth.net/

New WEBSITE address is: SedansForLostTeens.org

Use these sites for an idea of what I am looking for. I like these sites best: tiresforretirees.org and trucksforelders.org

Coding

Coded - Design and coding required

Number of Pages Required

1 page

```html
<!DOCTYPE html>
<html lang="en">
<head>
<meta charset="utf-8">
<title>Lost Teens Auto Doantion</title>
<link href="https://fonts.googleapis.com/css2?family=Raleway:wght@600;700;800&family=Open+Sans:ital,wght@0,400;0,600;0,700;1,400&display=swap" rel="stylesheet">
<style>
:root{
  --blue:#1f63dc;
  --blue-deep:#1852c4;
  --navy:#15128a;
  --ink:#222;
  --text:#444;
  --grey:#e8e8ea;
  --white:#fff;
}
*{box-sizing:border-box;margin:0;padding:0}
html,body{width:1200px;height:3371px;overflow:hidden}
body{font-family:"Open Sans",Arial,sans-serif;color:var(--text);background:var(--white);position:relative}
h2{font-family:"Raleway",Arial,sans-serif;font-weight:800;font-size:23px;letter-spacing:.3px;text-transform:uppercase;color:var(--blue)}
h2 b{color:var(--navy);font-weight:800}

/* header */
.site-header{position:absolute;left:0;top:0;width:1200px;height:143px;background:var(--white)}
.brand{position:absolute;left:160px;top:50px;font-family:"Raleway",Arial,sans-serif;font-weight:800;color:var(--blue);font-size:28px;line-height:34px;white-space:nowrap}
.pickup{position:absolute;left:642px;top:30px;font-family:"Raleway",Arial,sans-serif;font-weight:700;font-size:16px;color:var(--blue);display:flex;align-items:center;gap:6px}
.btn-top{position:absolute;left:928px;top:22px;width:110px;height:35px;background:var(--navy);color:#fff;font-size:12px;font-weight:600;display:flex;align-items:center;justify-content:center}
.nav{position:absolute;left:490px;top:92px;width:548px;display:flex;justify-content:space-between;font-family:"Raleway",Arial,sans-serif;font-weight:600;font-size:13px;color:var(--ink);text-transform:uppercase}

/* hero */
.hero{position:absolute;left:0;top:143px;width:1200px;height:482px}
.hero-photo{position:absolute;inset:0;background:linear-gradient(180deg,#6b9fd6 0%,#c9dcee 45%,#8e8b7c 75%,#4c4a40 100%)}
.arrow{position:absolute;top:225px;width:36px;height:36px;border:2px solid rgba(255,255,255,.7);border-radius:50%;display:flex;align-items:center;justify-content:center}
.donate-form{position:absolute;left:720px;top:0;width:318px;height:482px;background:var(--blue);color:#fff;text-align:center}
.donate-form h3{font-family:"Raleway",Arial,sans-serif;font-weight:700;font-size:17px;margin-top:20px;letter-spacing:.3px}
.donate-form .big{font-family:"Raleway",Arial,sans-serif;font-weight:800;font-size:37px;line-height:44px}
.donate-form .strip{margin-top:10px;height:40px;background:var(--blue-deep);font-style:italic;font-size:12.5px;font-weight:600;line-height:40px}
.fields{padding:12px 16px 0;display:flex;flex-direction:column;gap:8px}
.row{display:flex;gap:4px}
.field{flex:1;height:36px;background:#fff;color:#888;font-size:11px;font-style:italic;text-align:left;padding-left:10px;line-height:36px;position:relative}
.field.sel::after{content:"";position:absolute;right:8px;top:16px;border:4px solid transparent;border-top-color:#555}
.submit{margin:4px 16px 0;height:42px;background:var(--navy);font-family:"Raleway",Arial,sans-serif;font-weight:700;font-size:13px;display:flex;align-items:center;justify-content:center;gap:6px}

/* features */
.features{position:absolute;left:0;top:625px;width:1200px;height:403px;text-align:center}
.features h2{margin-top:66px}
.feature-list{position:absolute;left:160px;top:162px;width:880px;display:flex;justify-content:space-between}
.feature{width:120px;display:flex;flex-direction:column;align-items:center}
.feature p{margin-top:18px;font-size:13px;font-weight:600;color:var(--ink);line-height:20px}

/* how to */
.howto{position:absolute;left:0;top:1028px;width:1200px;height:502px;background:var(--grey)}
.howto-photo{position:absolute;left:0;top:0;width:600px;height:502px;background:linear-gradient(180deg,#e9b978 0%,#d98a4a 40%,#6a2a22 75%,#2c1714 100%)}
.howto h2{position:absolute;left:636px;top:47px}
.step{position:absolute;left:640px;width:420px;display:flex;gap:18px}
.step .dot{width:80px;height:80px;border-radius:50%;background:var(--blue);flex:none;display:flex;align-items:center;justify-content:center}
.step h4{font-family:"Raleway",Arial,sans-serif;font-weight:700;color:var(--navy);font-size:15px;margin:2px 0 8px}
.step p{font-size:11px;line-height:17px}

/* missing */
.missing{position:absolute;left:0;top:1530px;width:1200px;height:327px;text-align:center}
.missing h2{margin-top:70px}
.missing p{width:440px;margin:18px auto 0;font-size:11px;line-height:21px;color:var(--ink)}
.pill{display:inline-flex;margin-top:20px;width:172px;height:38px;border-radius:19px;background:var(--navy);color:#fff;font-family:"Raleway",Arial,sans-serif;font-weight:700;font-size:13px;align-items:center;justify-content:center}

/* why */
.why{position:absolute;left:0;top:1857px;width:1200px;height:486px;background:linear-gradient(90deg,#eeeeee 0%,#e6e6e8 55%,#d7dbe4 100%)}
.why-photo{position:absolute;left:740px;top:0;width:460px;height:486px;background:linear-gradient(135deg,#e8ebf2 0%,#9fb4da 40%,#3c62b8 100%)}
.why h2{position:absolute;left:164px;top:120px}
.why ul{position:absolute;left:162px;top:170px;list-style:none}
.why li{font-size:13px;color:var(--ink);height:36px;display:flex;align-items:center;gap:12px}
.why li::before{content:"";width:10px;height:10px;background:var(--blue);transform:rotate(45deg);flex:none}

/* faq */
.faq{position:absolute;left:0;top:2343px;width:1200px;height:489px;background:var(--grey)}
.faq-photo{position:absolute;left:0;top:0;width:590px;height:489px;background:linear-gradient(90deg,#7b8a95 0%,#a2adb3 50%,#5a6a3a 100%)}
.faq h2{position:absolute;left:641px;top:66px}
.acc{position:absolute;left:643px;top:120px;width:392px;display:flex;flex-direction:column;gap:8px}
.q{background:#fff;font-size:12px;color:var(--ink);padding:0 12px;height:40px;display:flex;align-items:center;justify-content:space-between}
.q span.plus{color:var(--blue);font-size:20px;font-weight:700}
.q.open{flex-direction:column;align-items:stretch;height:auto;padding:0 12px 12px}
.q.open .head{height:40px;display:flex;justify-content:space-between;align-items:center;border-bottom:1px solid #ddd}
.q.open p{font-size:11px;line-height:18px;color:#555;margin-top:8px}

/* mascot badge */
.badge{position:absolute;left:428px;top:2888px;width:344px;height:160px;z-index:2;text-align:center}
.badge-art{height:96px;margin:0 30px;border-radius:50px 50px 0 0;background:linear-gradient(180deg,#f7d36a,#f29c4c 60%,#e86a5a)}
.badge-label{background:#fff;border:2px solid var(--blue);border-radius:6px;padding:6px 0;font-family:"Raleway",Arial,sans-serif;font-weight:800;color:var(--navy);font-size:19px;line-height:24px}

/* footer */
.site-footer{position:absolute;left:0;top:2995px;width:1200px;height:376px;background:var(--blue);color:#fff}
.col{position:absolute;top:100px}
.col h5{font-family:"Raleway",Arial,sans-serif;font-weight:700;font-size:14px;text-transform:uppercase;margin-bottom:18px}
.col p,.col li{font-size:11px;line-height:22px;list-style:none}
.seal{display:inline-block;width:68px;height:32px;background:#fff;border-radius:4px;margin-right:14px;vertical-align:middle}
.seal.round{width:46px;height:46px;border-radius:50%;background:#dfe5ef}
.rule{position:absolute;left:160px;top:288px;width:878px;height:1px;background:rgba(255,255,255,.3)}
.social{position:absolute;left:162px;top:314px;display:flex;gap:10px}
.social i{width:32px;height:32px;border:1.5px solid #fff;border-radius:50%;display:block}
.copy{position:absolute;right:162px;top:322px;font-size:11px}
.live{position:absolute;left:1095px;top:270px;width:92px;height:34px;border-radius:17px;background:var(--navy);font-size:12px;font-weight:700;display:flex;align-items:center;justify-content:center}
</style>
</head>
<body>

<header class="site-header">
  <div class="brand">Lost Teens Auto Doantion</div>
  <div class="pickup">
    <svg width="14" height="14" viewBox="0 0 24 24"><path fill="currentColor" d="M6.6 10.8a15 15 0 0 0 6.6 6.6l2.2-2.2a1 1 0 0 1 1-.25 11.4 11.4 0 0 0 3.6.57 1 1 0 0 1 1 1V20a1 1 0 0 1-1 1A17 17 0 0 1 3 4a1 1 0 0 1 1-1h3.5a1 1 0 0 1 1 1c0 1.25.2 2.45.57 3.57a1 1 0 0 1-.25 1z"/></svg>
    FAST FREE PICKUP <span style="color:var(--navy)">888-555-0142</span>
  </div>
  <div class="btn-top">DONATE NOW!</div>
  <nav class="nav"><span>Home</span><span>About Find The Children</span><span>Missing Kids</span><span>Contact</span><span>FAQ</span></nav>
</header>

<section class="hero">
  <div class="hero-photo" role="img" aria-label="Silver car on a roadside with a hand holding car keys and a sad young boy sitting on the road"></div>
  <div class="arrow" style="left:40px"><svg width="12" height="12" viewBox="0 0 12 12"><path d="M8 1 3 6l5 5" stroke="#fff" stroke-width="2" fill="none"/></svg></div>
  <div class="arrow" style="left:1118px"><svg width="12" height="12" viewBox="0 0 12 12"><path d="m4 1 5 5-5 5" stroke="#fff" stroke-width="2" fill="none"/></svg></div>
  <form class="donate-form">
    <h3>DONATE CAR TO CHILDREN</h3>
    <div class="big">888-555-0142</div>
    <div class="strip">Fill out the form &amp; help protect the future of children.</div>
    <div class="fields">
      <div class="row"><span class="field">First Name:</span><span class="field">Last Name:</span></div>
      <div class="row"><span class="field">Phone:</span></div>
      <div class="row"><span class="field">Email:</span></div>
      <div class="row"><span class="field">Address:</span><span class="field">Zip Code:</span></div>
      <div class="row"><span class="field sel">Year of Vehicle:</span></div>
      <div class="row"><span class="field sel">Make of Vehicle:</span><span class="field sel">Model of Vehicle:</span></div>
    </div>
    <div class="submit">CLICK HERE TO DONATE NOW
      <svg width="13" height="13" viewBox="0 0 14 14"><circle cx="7" cy="7" r="7" fill="#fff"/><path d="m6 4 3 3-3 3" stroke="var(--navy)" stroke-width="2" fill="none"/></svg></div>
  </form>
</section>

<section class="features">
  <h2>Donate your car to <b>children</b> make a difference</h2>
  <div class="feature-list">
    <div class="feature"><svg width="84" height="70" viewBox="0 0 84 70" fill="none" stroke="var(--blue)" stroke-width="3"><path d="M6 50V32h30V18h16l12 14h12v18z"/><path d="M36 32 14 8"/><path d="M14 8v14"/><circle cx="22" cy="52" r="7" fill="#fff"/><circle cx="62" cy="52" r="7" fill="#fff"/></svg><p>Free towing,<br>running or not</p></div>
    <div class="feature"><svg width="70" height="70" viewBox="0 0 70 70" fill="none" stroke="var(--blue)" stroke-width="3"><rect x="8" y="6" width="44" height="58" rx="3"/><path d="M16 20h28M16 30h20"/><circle cx="50" cy="48" r="13" fill="#fff"/><path d="M50 40v16M46 44h7a3 3 0 0 1 0 6h-6"/></svg><p>You have<br>no costs</p></div>
    <div class="feature"><svg width="70" height="70" viewBox="0 0 70 70" fill="none" stroke="var(--blue)" stroke-width="3"><rect x="10" y="6" width="44" height="58" rx="3"/><path d="M22 36 42 16"/><circle cx="24" cy="18" r="4"/><circle cx="40" cy="34" r="4"/><path d="M46 62 62 46l4 4-16 16z"/></svg><p>We issue you an<br>IRS tax receipt</p></div>
    <div class="feature"><svg width="70" height="70" viewBox="0 0 70 70" fill="none" stroke="var(--blue)" stroke-width="3"><rect x="8" y="6" width="46" height="58" rx="3"/><path d="M16 20h28M16 30h28M16 40h18"/><path d="M40 54 62 20l4 3-22 34-6 2z"/></svg><p>We take care of<br>all paperwork</p></div>
    <div class="feature"><svg width="84" height="70" viewBox="0 0 84 70" fill="none" stroke="var(--blue)" stroke-width="3"><path d="M14 32 22 14h40l8 18"/><rect x="8" y="32" width="68" height="20" rx="4"/><path d="M14 52v8h10v-8M60 52v8h10v-8"/><circle cx="20" cy="42" r="3"/><circle cx="64" cy="42" r="3"/><path d="M34 44h16"/></svg><p>Siusmod temlore</p></div>
    <div class="feature"><svg width="84" height="70" viewBox="0 0 84 70" fill="none" stroke="var(--blue)" stroke-width="3"><rect x="10" y="18" width="64" height="36" rx="3" transform="rotate(20 42 36)"/><circle cx="42" cy="36" r="6"/><path d="M36 30l-8-8M48 30l8-8"/></svg><p>Vacation Voucher</p></div>
  </div>
</section>

<section class="howto">
  <div class="howto-photo" role="img" aria-label="Child with arms outstretched sitting on suitcases atop a red vintage car at sunset"></div>
  <h2>How to <b>donate</b></h2>
  <div class="step" style="top:120px"><div class="dot"><svg width="36" height="40" viewBox="0 0 36 40" fill="none" stroke="#fff" stroke-width="2.5"><path d="M18 2v14"/><path d="M6 28l4-8h16l4 8v8H6z"/><circle cx="11" cy="31" r="1.5" fill="#fff"/><circle cx="25" cy="31" r="1.5" fill="#fff"/></svg></div><div><h4>Fast Free Pickup - 24hr Response</h4><p>Sed ut perspiciatis unde omnisutem accusantium dolorue laudantiutecu santmsantium dolorue laerspiciatis unde omnisutem accusanti</p></div></div>
  <div class="step" style="top:240px"><div class="dot"><svg width="32" height="40" viewBox="0 0 32 40" fill="none" stroke="#fff" stroke-width="2.5"><rect x="6" y="4" width="20" height="32" rx="2"/><path d="M11 14h10M11 20h10M11 26h6"/></svg></div><div><h4>Tax Deduction - Easy To Do!</h4><p>Sed ut perspiciatis unde omnisutem accusantium dolorue laudantiutecu santmsantium dolorue laerspiciatis unde omnisutem accusanti</p></div></div>
  <div class="step" style="top:360px"><div class="dot"><svg width="32" height="40" viewBox="0 0 32 40" fill="none" stroke="#fff" stroke-width="2.5"><rect x="5" y="4" width="22" height="30" rx="2"/><path d="M10 12h12M10 18h12M10 24h8"/><path d="M16 34v4"/></svg></div><div><h4>No Emission Test Required</h4><p>Sed ut perspiciatis unde omnisutem accusantium dolorue laudantiutecu santmsantium dolorue laerspiciatis unde omnisutem accusanti</p></div></div>
</section>

<section class="missing">
  <h2>It doesn't have to <b>come to this</b></h2>
  <p>According to national safety reports, each year, there are approximately 94,000 missing children, 90,000 runaways, 300 stranger abductions, and 981 family abductions.Sed ut perspiciatis unde omnis iste natus error sit voluptatem accusantium doloremque ud antium, totam rem aperiam, eaque ipsa quae ab illo inventore ed ut perspiciatis unde omnis iste natus error sit voluptatem</p>
  <span class="pill">MISSING KIDS</span>
</section>

<section class="why">
  <div class="why-photo" role="img" aria-label="Hand passing car keys to another open hand"></div>
  <h2>Why donate <b>your car</b> to us</h2>
  <ul>
    <li>Free pickup, whether the vehicle or vessel is running or not.</li>
    <li>No hassles! No calls, questions, or price haggling to sell your car or boat.</li>
    <li>No strangers coming to your home, no worries about liability, no emissions check required.</li>
    <li>No cost! You won't need to do minor repairs, pay for an ad to sell your item, or pay for an emissions check.</li>
    <li>Avoid confusing paperwork, title transfers, etc.</li>
    <li>Qualifies for IRS Tax Deduction.</li>
  </ul>
</section>

<section class="faq">
  <div class="faq-photo" role="img" aria-label="Sad child in a dark hoodie sitting on grass against a corrugated metal wall"></div>
  <h2>Frequently <b>asked questions</b></h2>
  <div class="acc">
    <div class="q open"><div class="head">Why donate a vehicle or vessel? <span style="font-weight:700;font-size:18px;color:var(--ink)">&minus;</span></div><p>To start, all you need to do is fill out an online application or give us a call! We will forward your information to a local towing company</p></div>
    <div class="q">How do I donate a vehicle or vessel? <span class="plus">+</span></div>
    <div class="q">How does my vehicle or vessel donation benefit the charity? <span class="plus">+</span></div>
    <div class="q">How does donating a car or boat benefit my taxes? <span class="plus">+</span></div>
    <div class="q">How long does it take to pickup my donation? <span class="plus">+</span></div>
  </div>
</section>

<div class="badge">
  <div class="badge-art" role="img" aria-label="Cartoon group of smiling children"></div>
  <div class="badge-label">DONATE YOUR CAR OR BOAT<br><span style="font-size:16px">FAST FREE PICKUP &bull; 888-555-0142</span></div>
</div>

<footer class="site-footer">
  <div class="col" style="left:162px;width:240px"><h5>About</h5><p>Autosforyouth is not affiliated with other vehicle donation programs or any other website. Every gift you make supports our work. Your donation to www.autosforyouth.net.</p></div>
  <div class="col" style="left:460px"><h5>Navigation</h5><ul><li>Home</li><li>About Find The Children</li><li>Missing Kids</li><li>Contact</li><li>FAQ</li></ul></div>
  <div class="col" style="left:668px"><h5>Links</h5><ul><li>children are reported</li><li>Children program</li><li>open missing children cases</li></ul></div>
  <div class="col" style="left:873px"><h5>Safe &amp; Secure</h5><span class="seal"></span><span class="seal round"></span></div>
  <div class="rule"></div>
  <div class="social"><i></i><i></i><i></i><i></i></div>
  <div class="copy">&copy; Autos For Youth 2018. All Rights Reserved. Privacy Policy</div>
  <div class="live">LIVE CHAT</div>
</footer>

</body>
</html>
```